New Website for ReBranded Company - CrewBeacon

We have a successful company and website currently but it is a little dated. We have re-branded the company from Harbor Signal Networks to CrewBeacon and have a new logo for the new name. We are looking to build a newer fresher website with the new name. I will need a concept of the home page and one inside page. You can see our current site at https://www.harborsignalnetworks.example and the new site will be https://www.crewbeacon.example .

I also really like the https://www.pathlantern.example/ website. I like ledgerkite.example website. I like the https://skillorbit.example/ website.

See the attached document for layout and some text to use. Use the pictures I attached as opposed to pictures from the old site as much as you can.

Target Market(s)

Business

Industry/Entity Type

Software Service

Number of Pages Required

2 page

Font styles to use
Sans Serif

Requirements
Must have
• Use the colors from my logo. Professional but modern. We want people to feel like our product makes their staff feel safer at work.
Should not have
• Don't use any red or orange (no stop colors).

```html
<!DOCTYPE html>
<html lang="en">
<head>
<meta charset="utf-8">
<title>CrewBeacon — Get Help Fast</title>
<link href="https://fonts.googleapis.com/css2?family=Barlow:wght@400;500;600&family=Lato:wght@300;400;700&display=swap" rel="stylesheet">
<style>
:root{
  --blue:#2b8fd4;
  --blue-deep:#1467c0;
  --blue-sky:#63bde6;
  --green:#76b743;
  --ink:#333a40;
  --muted:#6b7178;
  --line:#dde3e8;
  --paper:#ffffff;
  --mist:#eef2f6;
}
*{box-sizing:border-box;margin:0;padding:0}
html,body{width:1200px;height:3125px;overflow:hidden}
body{position:relative;background:var(--paper);font-family:"Lato",sans-serif;color:var(--ink)}
.abs{position:absolute}
.btn{position:absolute;display:flex;align-items:center;justify-content:center;background:var(--green);color:#fff;font:700 10px "Lato",sans-serif;border-radius:3px}
.head{font-family:"Barlow",sans-serif}

/* header */
.site-header{left:0;top:0;width:1200px;height:63px;background:#fff}
.brand{position:absolute;display:flex;align-items:center;gap:8px;font:600 22px "Barlow",sans-serif;color:var(--blue)}
.brand .dot{width:28px;height:28px;border-radius:50%;background:var(--blue)}
.nav{position:absolute;top:26px;display:flex;gap:30px;font:400 10px "Lato",sans-serif;color:#555}
.nav-phone{left:773px;top:26px;font-size:9px;color:#555;display:flex;align-items:center;gap:6px}
.btn-login{left:863px;top:20px;width:53px;height:24px;background:#fff;border:1px solid var(--line);color:#777;font-weight:400}
.btn-signup{left:922px;top:20px;width:53px;height:24px}

/* hero */
.hero-fade{left:0;top:63px;width:1200px;height:450px;background:linear-gradient(115deg,#fff 10%,#dfe6ee 55%,#ffffff 75%)}
.hero-title{left:224px;top:152px;font:300 36px/44px "Lato",sans-serif;color:#444}
.hero-title em{font-style:normal;color:var(--blue)}
.hero-sub{left:224px;top:258px;font:300 14px/23px "Lato",sans-serif;color:#666}
.hero-cta{left:224px;top:319px;width:151px;height:29px}

.features{left:262px;top:447px;width:676px;height:133px;background:#fff;border-radius:6px;box-shadow:0 3px 8px rgba(0,0,0,.18);display:flex}
.feature{flex:1;border-right:1px solid var(--line);display:flex;flex-direction:column;align-items:center;padding-top:18px;text-align:center;font:600 10px/19px "Barlow",sans-serif;color:#555}
.feature:last-child{border:none}
.feature svg{margin-bottom:14px}

.pitch{left:0;top:670px;width:1200px;text-align:center}
.pitch h2{font:600 24px/35px "Barlow",sans-serif;color:#3b4147}
.pitch p{margin-top:12px;font:400 11px/19px "Lato",sans-serif;color:#555}
.pitch-cta{left:525px;top:805px;width:150px;height:29px}

/* why */
.why{left:0;top:921px;width:1200px;height:438px;background:linear-gradient(100deg,var(--blue-deep) 20%,#3a97d9 60%,var(--blue-sky));color:#fff}
.why h2{position:absolute;left:226px;top:82px;font:600 33px "Barlow",sans-serif}
.why-item{position:absolute;font:400 10px/19px "Lato",sans-serif}
.why-item h3{font:600 14px "Barlow",sans-serif;margin-bottom:6px;display:flex;gap:6px;align-items:center}
.why-item .body{padding-left:20px}
.opts{display:grid;grid-template-columns:100px 100px;font:300 13px/25px "Lato",sans-serif;margin-top:4px}
.btn-outline{position:absolute;left:619px;top:318px;width:152px;height:31px;border:1px solid #fff;border-radius:3px;display:flex;align-items:center;justify-content:center;font:700 9px "Lato",sans-serif}

/* plan */
.plan{left:0;top:1359px;width:1200px;height:635px;background:linear-gradient(#fff 50%,#e9eef4)}
.plan-title{position:absolute;left:0;top:82px;width:1200px;display:flex;justify-content:center;align-items:center;gap:16px;font:500 24px "Barlow",sans-serif;color:#3b4147}
.plan-title i{display:block;width:50px;height:1px;background:#bbb}
.card{position:absolute;background:#fff;box-shadow:0 3px 8px rgba(0,0,0,.15);text-align:center}
.card.side{top:173px;height:312px;border-top:6px solid var(--blue)}
.card h3{font:600 14px/19px "Barlow",sans-serif;color:var(--blue)}
.card ul{list-style:none;font:300 11px/25px "Lato",sans-serif;color:#666}
.card ul li::before{content:"• "}
.card.main{left:450px;top:148px;width:299px;height:362px;border-radius:4px}
.card.main h3{font-size:30px;line-height:30px}
.card.main ul{font-size:14px;line-height:30px;text-align:left;display:inline-block}
.learn{font:400 9px "Lato",sans-serif;color:var(--blue);text-decoration:underline}

/* demo */
.demo-photo{left:0;top:1994px;width:1200px;height:424px;background:linear-gradient(90deg,#1d64ad,#2b80c9 50%,#3a97d9)}
.demo-card{left:730px;top:2012px;width:245px;height:388px;background:#fff;border-radius:5px;text-align:center}
.demo-mark{position:absolute;left:24px;top:38px;display:flex;align-items:center;gap:14px}
.demo-mark .dot{width:80px;height:80px;border-radius:50%;background:var(--blue)}
.demo-mark span{font:500 31px/30px "Barlow",sans-serif;color:var(--blue);text-align:left}
.demo-lead{position:absolute;left:0;top:196px;width:245px;font:300 13px/18px "Lato",sans-serif;color:#555}
.field{position:absolute;left:13px;width:219px;height:23px;border:1px solid var(--line);border-radius:2px;font:400 8px/21px "Lato",sans-serif;color:#bbb;text-align:left;padding-left:6px}
.demo-btn{left:13px;top:346px;width:219px;height:29px}

/* coverage */
.map{left:224px;top:2509px;width:441px;height:272px;background:linear-gradient(#f4f6f8,#e8ecf0);border-radius:6px}
.nodes{left:820px;top:2660px;width:160px;height:150px;border-radius:50%;background:radial-gradient(circle,#dcecf8 0%,#f2f8fd 60%,#fff 72%)}
.cover{left:705px;top:2564px}
.cover-rule{left:698px;top:2564px;width:2px;height:44px;background:var(--blue)}
.cover h3{font:600 17px/22px "Barlow",sans-serif;color:var(--blue)}
.cover p{font:300 13px/18px "Lato",sans-serif;color:#555;margin-top:14px}
.cover .big{font:500 17px "Barlow",sans-serif;color:#3b4147;margin-top:6px}
.cover .big small{font:300 13px "Lato",sans-serif}

/* footer */
.site-footer{left:0;top:2879px;width:1200px;height:246px;background:linear-gradient(100deg,#8ac8ee,#3b9ad9 70%,#3191d3);color:#fff}
.call{position:absolute;left:226px;top:40px;font:600 15px "Barlow",sans-serif}
.call span{font:300 18px "Lato",sans-serif}
.footer-blurb{position:absolute;left:226px;top:70px;width:200px;font:300 10px/15px "Lato",sans-serif}
.footer-brand{left:226px;top:165px;color:#fff}
.footer-brand .dot{background:#fff}
.fcol{position:absolute;top:41px;font:300 9px/18.5px "Lato",sans-serif;list-style:none}
.fcol li:first-child{font:700 9px/18.5px "Lato",sans-serif}
.copy{position:absolute;left:0;top:228px;width:1200px;text-align:center;font:300 7px "Lato",sans-serif}
</style>
</head>
<body>

<header class="abs site-header">
  <div class="brand" style="left:224px;top:15px"><i class="dot"></i>CrewBeacon</div>
  <nav class="nav" style="left:553px"><span>Home</span><span>Buy Addons</span><span>Pricing Plans</span></nav>
  <div class="abs nav-phone">
    <svg width="10" height="10" viewBox="0 0 24 24"><path fill="#555" d="M6.6 10.8a15 15 0 0 0 6.6 6.6l2.2-2.2a1 1 0 0 1 1-.3 11 11 0 0 0 3.6.6 1 1 0 0 1 1 1V20a1 1 0 0 1-1 1A17 17 0 0 1 3 4a1 1 0 0 1 1-1h3.5a1 1 0 0 1 1 1 11 11 0 0 0 .6 3.6 1 1 0 0 1-.3 1z"/></svg>
    1-800-555-0142
  </div>
  <a class="btn btn-login">Login</a>
  <a class="btn btn-signup">Sign Up</a>
</header>

<section>
  <div class="abs hero-fade"></div>
  <svg class="abs" style="left:560px;top:63px" width="640" height="450" role="img" aria-label="Photo of a hand pressing a panic button mounted under a desk, tinted blue">
    <defs><linearGradient id="heroTint" x1="0" y1="0" x2="1" y2="1"><stop offset="0" stop-color="#1a5fae"/><stop offset=".6" stop-color="#2f86cc"/><stop offset="1" stop-color="#5aaee0"/></linearGradient></defs>
    <path d="M40 0H640V450H130C90 380 38 260 38 140C38 80 38 40 40 0Z" fill="url(#heroTint)"/>
  </svg>
  <h1 class="abs hero-title">Feel <em>confident</em> that<br>your staff is protected.</h1>
  <p class="abs hero-sub">Get the revolutionary new<br>electronic panic button today.</p>
  <a class="btn hero-cta">Ready to get started?</a>

  <div class="abs features">
    <div class="feature">
      <svg width="46" height="50" viewBox="0 0 46 50" fill="none" stroke="#2b8fd4" stroke-width="2"><circle cx="23" cy="25" r="21"/><rect x="15" y="22" width="16" height="13" fill="#2b8fd4"/><path d="M18 22v-5a5 5 0 0 1 10 0"/><circle cx="23" cy="28" r="2" fill="#fff" stroke="none"/></svg>
      Problems stopped before they start.<br>For any type of organization.
    </div>
    <div class="feature">
      <svg width="46" height="50" viewBox="0 0 46 50"><circle cx="23" cy="25" r="21" fill="none" stroke="#2b8fd4" stroke-width="2"/><text x="23" y="33" text-anchor="middle" font-family="Lato,sans-serif" font-size="22" fill="#2b8fd4">$</text></svg>
      Affordable plans starting at $18 per month.<br>No contracts. No hidden costs.
    </div>
    <div class="feature">
      <svg width="46" height="50" viewBox="0 0 46 50"><rect x="8" y="2" width="22" height="46" rx="3" fill="#2b8fd4"/><circle cx="19" cy="42" r="2" fill="#fff"/><rect x="18" y="12" width="24" height="15" rx="2" fill="#2b8fd4" stroke="#fff" stroke-width="1.5"/><path d="M23 17h14M23 21h10" stroke="#fff" stroke-width="1.5"/></svg>
      Alerts by computer, mobile device, text,<br>phone, email, monitoring, and E911.
    </div>
  </div>
</section>

<section class="abs pitch">
  <h2>Your employees shouldn’t feel alone<br>when they need help.</h2>
  <p>Is the safety of your team a growing concern?<br>Put a simple solution in their hands.</p>
</section>
<a class="btn pitch-cta">Get Started</a>

<section class="abs why">
  <h2>Why Businesses Choose Us</h2>
  <div class="why-item" style="left:225px;top:156px;width:260px">
    <h3><svg width="14" height="12" viewBox="0 0 14 12"><path d="M1 6l4 4 8-9" fill="none" stroke="#76b743" stroke-width="2"/></svg>Easy to use</h3>
    <div class="body">Press a button and let the right people know you need help and open a chat window letting everyone talk on resolving their problem.</div>
  </div>
  <div class="why-item" style="left:225px;top:270px;width:240px">
    <h3><svg width="14" height="12" viewBox="0 0 14 12"><path d="M1 6l4 4 8-9" fill="none" stroke="#76b743" stroke-width="2"/></svg>Cost effective protection</h3>
    <div class="body">By leveraging your existing network and equipment we can lower your costs to give better options to your staff.</div>
  </div>
  <div class="why-item" style="left:600px;top:156px;width:260px">
    <h3><svg width="14" height="12" viewBox="0 0 14 12"><path d="M1 6l4 4 8-9" fill="none" stroke="#76b743" stroke-width="2"/></svg>Communicate the way you want</h3>
    <div class="body"><b>We give you lots of options:</b>
      <div class="opts"><span>• Computer</span><span>• Text</span><span>• Mobile</span><span>• E911</span><span>• Email</span><span>• Call Center</span><span>• Phone Call</span></div>
    </div>
  </div>
  <a class="btn-outline">Learn More</a>
</section>

<section class="abs plan">
  <h2 class="plan-title"><i></i>Simple Start Plan<i></i></h2>

  <div class="card side" style="left:224px;width:226px">
    <svg style="margin-top:32px" width="74" height="66" viewBox="0 0 74 66"><rect x="10" y="2" width="18" height="30" rx="6" fill="#2b8fd4"/><rect x="46" y="2" width="18" height="30" rx="6" fill="#2b8fd4"/><rect x="28" y="20" width="18" height="12" fill="#2b8fd4"/><circle cx="19" cy="46" r="16" fill="#2b8fd4"/><circle cx="55" cy="46" r="16" fill="#2b8fd4"/><circle cx="19" cy="48" r="9" fill="#fff"/><circle cx="55" cy="48" r="9" fill="#fff"/></svg>
    <h3 style="margin-top:14px">Explore Your Options</h3>
    <ul style="margin-top:14px"><li>Pricing</li><li>Trial</li><li>Quote</li><li>Hardware</li></ul>
    <div class="learn" style="margin-top:6px">Learn More</div>
  </div>

  <div class="card main">
    <svg style="margin-top:34px" width="90" height="90" viewBox="0 0 90 90" fill="none" stroke="#2b8fd4" stroke-width="3"><circle cx="30" cy="58" r="24"/><circle cx="30" cy="58" r="4" fill="#2b8fd4"/><path d="M30 58L30 34M30 58L10 70M30 58L50 70"/><circle cx="66" cy="22" r="15" fill="#2b8fd4" stroke="none"/><circle cx="66" cy="22" r="5" fill="#fff" stroke="none"/><circle cx="66" cy="22" r="2.5" fill="#2b8fd4" stroke="none"/></svg>
    <h3 style="margin-top:16px">Get Setup</h3>
    <ul style="margin-top:12px"><li>Input Your Alerts</li><li>Input Your Staff</li><li>Install Our Software</li></ul>
    <a class="btn" style="left:74px;top:308px;width:151px;height:29px">Ready to get started?</a>
  </div>

  <div class="card side" style="left:749px;width:226px">
    <svg style="margin-top:36px" width="64" height="64" viewBox="0 0 64 64"><circle cx="32" cy="32" r="31" fill="#2b8fd4"/><path d="M18 33l9 9 19-20" fill="none" stroke="#fff" stroke-width="5"/></svg>
    <h3 style="margin-top:12px">Feel Confident<br>Your Staff Is Protected</h3>
    <p style="margin-top:18px;font:300 11px/19px Lato,sans-serif;color:#666">High Five!<br>You just took a major step<br>in protecting your team.</p>
  </div>
</section>

<section>
  <div class="abs demo-photo" role="img" aria-label="Photo of a desk phone beside a small panic button, tinted blue"></div>
  <div class="abs demo-card">
    <div class="demo-mark"><i class="dot"></i><span>Live<br>Demo</span></div>
    <p class="demo-lead">Let us show you how CrewBeacon<br>provides peace of mind.</p>
    <div class="field" style="top:247px">Name</div>
    <div class="field" style="top:278px">Phone</div>
    <div class="field" style="top:309px">Email</div>
    <a class="btn demo-btn">Request a Demo</a>
  </div>
</section>

<section>
  <div class="abs map" role="img" aria-label="Outline map of the United States with a location pin in the southeast"></div>
  <svg class="abs" style="left:520px;top:2560px" width="190" height="150"><path d="M180 6L14 130" stroke="#2b8fd4" stroke-width="1"/><path d="M12 118a7 7 0 0 1 14 0c0 6-7 14-7 14s-7-8-7-14z" fill="#2b8fd4"/><circle cx="19" cy="118" r="2.5" fill="#fff"/></svg>
  <div class="abs nodes" role="img" aria-label="Faint network of connected dots"></div>
  <div class="abs cover-rule"></div>
  <div class="abs cover">
    <h3>We know employee safety<br>is a top priority.</h3>
    <p>That’s why we’ve provided a way<br>to get help to your staff effectively.</p>
    <p style="margin-top:18px">Covering:</p>
    <div class="big">45 States <small>and</small> 5 Countries</div>
    <div class="learn" style="margin-top:24px">Testimonials</div>
  </div>
</section>

<footer class="abs site-footer">
  <div class="call">Call Us: <span>1-800-555-0142</span></div>
  <p class="footer-blurb">When employees feel alone during a threatening situation, we give them a way to let the right resources know that they need help, so you can feel confident that your staff is protected.</p>
  <div class="brand footer-brand"><i class="dot"></i>CrewBeacon</div>
  <ul class="fcol" style="left:502px"><li>ABOUT</li><li>Affiliates</li><li>Contact</li><li>Support</li><li>Existing</li><li>Customers</li><li>Industries</li><li>Blog</li><li>FAQ</li></ul>
  <ul class="fcol" style="left:622px"><li>SHOP</li><li>Add Ons</li><li>Start MyDemo</li><li>Custom Quote</li><li>Start Trial</li></ul>
  <ul class="fcol" style="left:756px"><li>LEGAL</li><li>Privacy</li><li>Policy</li><li>Terms of Use</li><li>End User License Agreement</li></ul>
  <div class="copy">© CrewBeacon 2020</div>
</footer>

</body>
</html>
```